Designer and consultant for professionals/businesses and manufacturers in the kitchen and bath in...

I have 30 years of design experience, and 19 of those years within the marketing team of a national cabinet manufacturer. This role gave me the opportunity to consult and design for kitchen/bath businesses, from boutique to multi-store national scale. My services include layout and spatial planning, individual display design, and product design for cabinet manufacturers. From showrooms, to trade shows to integrated design collections. I would like to see designs that convey professionalism, as well as an appeal to the creative designer mind!

Target Market(s)

Kitchen and bath dealers, as well as mid-scale multi-store home centers. Cabinet manufacturers, Trade Show agencies.

Industry/Entity Type

Kitchen

Contact Information for Business Card

Serving Kitchen and Bath Businesses

Logo Text

MT (initials for business name)

Font styles to use
Serif
Sans Serif
Decorative

Colors
e34197

Requirements
Must have
• Marlowe Tavish Design and Consulting, Inc. (business name)
• marlowe@mtvantra.com (email)
• 917-555-0148 (phone)
• mtvantra.com (website)
Nice to have
• Inclusions of geometric shapes; particularly a 30/15 degree triangle and circle(s)
• 2 colors
Should not have
• Not too artsy!

```html
<!DOCTYPE html>
<html lang="en">
<head>
<meta charset="utf-8">
<title>Marlowe Tavish Design and Consulting – Business Card</title>
<link rel="stylesheet" href="https://fonts.googleapis.com/css2?family=Tinos:wght@400;700&family=Montserrat:wght@400;500&family=Arimo:wght@400&display=swap">
<style>
  :root {
    --magenta: #ad2185;
    --charcoal: #3a4241;
    --ink: #3d3d3d;
    --paper: #ffffff;
    --backdrop: #e9e6e1;
    --serif: "Tinos", "Times New Roman", serif;
    --sans: "Montserrat", Arial, sans-serif;
    --contact: "Arimo", Arial, sans-serif;
  }
  * { margin: 0; padding: 0; box-sizing: border-box; }
  html, body { width: 900px; height: 1200px; overflow: hidden; }
  body { background: var(--backdrop); position: relative; }

  .card {
    position: absolute;
    left: 80px;
    width: 733px;
    border-radius: 24px;
    overflow: hidden;
    background: var(--paper);
    box-shadow: 0 6px 14px rgba(0,0,0,0.22);
  }
  .card--front { top: 128px; height: 428px; }
  .card--back  { top: 646px; height: 429px; }
  .card-shapes { position: absolute; inset: 0; }

  .monogram {
    position: absolute;
    display: flex; align-items: center; justify-content: center;
    border-radius: 50%;
    font-family: var(--serif);
    font-weight: 400;
    letter-spacing: -2px;
  }
  .monogram--front {
    left: 296px; top: 52px; width: 140px; height: 140px;
    border: 3px solid var(--magenta);
    color: var(--charcoal);
    font-size: 62px;
  }
  .monogram--back {
    left: 528px; top: 192px; width: 164px; height: 164px;
    border: 4px solid var(--magenta);
    background: var(--paper);
    color: var(--charcoal);
    font-size: 74px;
  }

  .business-name {
    position: absolute; left: 0; right: 0; top: 203px;
    text-align: center;
    font-family: var(--serif); font-weight: 700;
    font-size: 26px; letter-spacing: 0.5px;
    color: var(--magenta);
  }
  .business-type {
    position: absolute; left: 0; right: 0; top: 236px;
    text-align: center;
    font-family: var(--serif); font-size: 18px;
    color: var(--ink);
  }

  .contact {
    position: absolute; top: 348px;
    display: flex; align-items: center; gap: 10px;
    font-family: var(--contact); font-size: 17px; color: var(--ink);
  }
  .contact--phone { left: 48px; }
  .contact--email { left: 258px; }
  .contact--web   { left: 546px; }
  .contact-icon { width: 24px; height: 24px; flex: none; }

  .headline {
    position: absolute; left: 0; right: 0; top: 68px;
    text-align: center;
    font-family: var(--serif); font-size: 26px; line-height: 36px;
    color: var(--ink);
  }
  .services {
    position: absolute; left: 46px; top: 222px;
    font-family: var(--sans); color: var(--ink);
  }
  .services-title { font-size: 19px; font-weight: 500; margin-bottom: 6px; }
  .services-list { list-style: none; font-size: 16.5px; line-height: 29px; }
  .services-list li::before {
    content: ""; display: inline-block;
    width: 9px; height: 9px; border-radius: 50%;
    background: var(--charcoal);
    margin: 0 8px 2px 2px; vertical-align: middle;
  }
  .tagline {
    position: absolute; left: 46px; top: 390px;
    font-family: var(--serif); font-size: 20px; color: var(--paper);
  }
  .tagline small { font-size: 18px; }
</style>
</head>
<body>

<section class="card card--front" aria-label="Business card front">
  <svg class="card-shapes" width="733" height="428" viewBox="0 0 733 428" aria-hidden="true">
    <polygon points="0,291 565,291 525,333 0,333" fill="var(--charcoal)"/>
    <polygon points="733,152 733,333 537,333" fill="var(--magenta)"/>
    <polygon points="0,387 460,387 420,428 0,428" fill="var(--charcoal)"/>
    <polygon points="480,387 733,387 733,428 440,428" fill="var(--magenta)"/>
  </svg>

  <div class="monogram monogram--front">MT</div>
  <h1 class="business-name">MARLOWE TAVISH</h1>
  <p class="business-type">Design and Consulting, Inc.</p>

  <div class="contact contact--phone">
    <svg class="contact-icon" viewBox="0 0 24 24" aria-hidden="true">
      <circle cx="12" cy="12" r="12" fill="var(--magenta)"/>
      <path d="M7 9.5c0-1.4 2.2-2.5 5-2.5s5 1.1 5 2.5v1h-2.3v-1.3h-5.4v1.3H7z" fill="#fff"/>
      <rect x="8" y="11.5" width="8" height="5" rx="1" fill="#fff"/>
    </svg>
    <span>917-555-0148</span>
  </div>
  <div class="contact contact--email">
    <svg class="contact-icon" viewBox="0 0 24 24" aria-hidden="true">
      <circle cx="12" cy="12" r="12" fill="var(--magenta)"/>
      <rect x="6.5" y="8" width="11" height="8" fill="#fff"/>
      <polyline points="6.5,8 12,12.5 17.5,8" fill="none" stroke="var(--magenta)" stroke-width="1.2"/>
    </svg>
    <span>marlowe@mtvantra.com</span>
  </div>
  <div class="contact contact--web">
    <svg class="contact-icon" viewBox="0 0 24 24" aria-hidden="true">
      <circle cx="12" cy="12" r="12" fill="var(--magenta)"/>
      <g fill="none" stroke="#fff" stroke-width="1.2">
        <circle cx="12" cy="12" r="6"/>
        <ellipse cx="12" cy="12" rx="2.6" ry="6"/>
        <line x1="6" y1="12" x2="18" y2="12"/>
        <line x1="7" y1="9" x2="17" y2="9"/>
        <line x1="7" y1="15" x2="17" y2="15"/>
      </g>
    </svg>
    <span>mtvantra.com</span>
  </div>
</section>

<section class="card card--back" aria-label="Business card back">
  <svg class="card-shapes" width="733" height="429" viewBox="0 0 733 429" aria-hidden="true">
    <polygon points="0,379 498,379 448,429 0,429" fill="var(--charcoal)"/>
    <polygon points="733,164 733,429 468,429" fill="var(--magenta)"/>
  </svg>

  <h2 class="headline">30 YEARS OF DESIGN AND MARKETING<br>FOR THE KITCHEN AND BATH INDUSTRY.</h2>

  <div class="services">
    <h3 class="services-title">Specializing in:</h3>
    <ul class="services-list">
      <li>Showroom design services, macro to micro</li>
      <li>Trade show display design</li>
      <li>Product design for industry manufacturers</li>
    </ul>
  </div>

  <div class="monogram monogram--back">MT</div>

  <p class="tagline">Serving Kitchen &amp; <small>Bath Businesses</small></p>
</section>

</body>
</html>
```